Business Card Design

Maple Crest Rentals
Maple Crest Rentals is a high end home rental leasing company that provides exquisite properties in niche markets. We are a small family owned business that considers our clients not as renters, but as friends. Every property we buy must be brought up to our high standards before it is offered on the market. The properties that we lease are exceptional, "move in" ready homes. This allows for the client to take pride in their lease as if it was their own home. To put it another way; we do not lease a property that we would not live in ourselves.

Target Market(s)

Couples making $100K or more

Industry/Entity Type

Business

Requirements
Must have
• Some sort of logo
Nice to have
• good slogan
Should not have
• Pink

```html
<!DOCTYPE html>
<html lang="en">
<head>
<meta charset="utf-8">
<title>Maple Crest Rentals — Business Card</title>
<link rel="stylesheet" href="https://fonts.googleapis.com/css2?family=Open+Sans:wght@400;600;700&display=swap">
<style>
  :root {
    --page-bg: #e9e6e1;
    --card-white: #fbfbfb;
    --brand-blue: #2e6fa6;
    --deep-blue: #0d3f78;
    --mid-blue: #1c5a9a;
    --leaf-green: #8cc63f;
    --band-text: #3f5a1c;
    --ink: #444a50;
    --rule: #6a9cc9;
    --white: #ffffff;
  }
  * { box-sizing: border-box; margin: 0; padding: 0; }
  html, body { width: 1200px; height: 1023px; overflow: hidden; }
  body {
    background: var(--page-bg);
    font-family: "Open Sans", Arial, sans-serif;
    display: flex;
    align-items: center;
    justify-content: center;
    gap: 40px;
  }
  .card {
    width: 540px;
    height: 309px;
    position: relative;
    border-radius: 3px;
    overflow: hidden;
    box-shadow: 0 6px 18px rgba(0,0,0,0.18);
  }

  /* Front */
  .card-front { background: var(--card-white); }
  .front-brand {
    position: absolute;
    top: 34px;
    right: 40px;
    display: flex;
    align-items: center;
    gap: 10px;
  }
  .brand-square {
    width: 22px; height: 22px;
    background: var(--brand-blue);
  }
  .brand-name {
    font-weight: 700;
    font-size: 26px;
    letter-spacing: 0.04em;
    text-transform: uppercase;
    color: var(--brand-blue);
  }
  .front-rule {
    position: absolute;
    top: 88px;
    left: 250px;
    right: 28px;
    height: 1px;
    background: var(--rule);
  }
  .holder {
    position: absolute;
    top: 118px;
    left: 34px;
  }
  .holder-name {
    font-weight: 700;
    font-size: 18px;
    color: var(--brand-blue);
    text-transform: uppercase;
  }
  .holder-title {
    font-size: 12px;
    color: var(--ink);
    margin-top: 2px;
    display: flex;
    align-items: center;
    gap: 6px;
  }
  .holder-title::before, .holder-title::after {
    content: "";
    height: 1px;
    background: var(--rule);
  }
  .holder-title::before { width: 12px; }
  .holder-title::after { width: 110px; }
  .contacts {
    position: absolute;
    top: 178px;
    left: 54px;
    list-style: none;
    font-size: 11.5px;
    color: var(--ink);
    line-height: 20px;
  }
  .contacts li { display: flex; align-items: center; gap: 8px; }
  .contacts svg { width: 12px; height: 12px; flex: none; }
  .office {
    position: absolute;
    top: 140px;
    left: 320px;
    font-size: 12px;
    color: var(--ink);
    line-height: 19px;
  }
  .office-name { font-weight: 600; color: var(--brand-blue); }
  .front-band {
    position: absolute;
    left: 0; right: 0; bottom: 0;
    height: 46px;
    background: var(--leaf-green);
    border-top: 2px solid var(--brand-blue);
    display: flex;
    align-items: center;
    justify-content: center;
  }
  .slogan {
    font-size: 11.5px;
    font-weight: 600;
    letter-spacing: 0.03em;
    text-transform: uppercase;
    color: var(--band-text);
  }

  /* Back */
  .card-back {
    background: linear-gradient(135deg, var(--mid-blue) 0%, var(--deep-blue) 70%, #0a3466 100%);
  }
  .back-brand {
    position: absolute;
    top: 118px;
    left: 0; right: 0;
    display: flex;
    align-items: center;
    justify-content: center;
    gap: 12px;
  }
  .back-brand .brand-square { background: var(--white); width: 26px; height: 26px; }
  .back-brand .brand-name { color: var(--white); font-size: 30px; }
  .services {
    position: absolute;
    bottom: 26px;
    left: 0; right: 0;
    text-align: center;
    font-size: 12px;
    color: var(--white);
    letter-spacing: 0.02em;
  }
</style>
</head>
<body>
  <section class="card card-front">
    <div class="front-brand">
      <span class="brand-square"></span>
      <span class="brand-name">Maple Crest Rentals</span>
    </div>
    <div class="front-rule"></div>

    <div class="holder">
      <p class="holder-name">Daniel Whitford</p>
      <p class="holder-title">Director</p>
    </div>

    <ul class="contacts">
      <li>
        <svg viewBox="0 0 12 12"><rect width="12" height="12" rx="2" fill="#2e6fa6"/><path d="M3.5 3h1.6l.6 1.6-.9.6a4.5 4.5 0 0 0 2 2l.6-.9 1.6.6V8.5c0 .3-.3.6-.6.6A6 6 0 0 1 3 3.6c0-.3.2-.6.5-.6z" fill="#fff"/></svg>
        215-555-0147
      </li>
      <li>
        <svg viewBox="0 0 12 12"><rect width="12" height="12" rx="2" fill="#2e6fa6"/><rect x="2.5" y="3.5" width="7" height="5" fill="none" stroke="#fff" stroke-width="0.9"/><path d="M2.5 3.5 6 6.3l3.5-2.8" fill="none" stroke="#fff" stroke-width="0.9"/></svg>
        daniel@maplecrestrentals.com
      </li>
      <li>
        <svg viewBox="0 0 12 12"><rect width="12" height="12" rx="2" fill="#2e6fa6"/><circle cx="6" cy="6" r="3.4" fill="none" stroke="#fff" stroke-width="0.9"/><path d="M2.6 6h6.8M6 2.6c-1.6 2-1.6 4.8 0 6.8M6 2.6c1.6 2 1.6 4.8 0 6.8" fill="none" stroke="#fff" stroke-width="0.8"/></svg>
        www.maplecrestrentals.com
      </li>
    </ul>

    <address class="office" style="font-style: normal;">
      <span class="office-name">Maple Crest Rentals Ltd.</span><br>
      48 Linden Ct<br>
      Ambler, PA 19002
    </address>

    <div class="front-band">
      <p class="slogan">We do not lease a property that we would not live in ourselves.</p>
    </div>
  </section>

  <section class="card card-back">
    <div class="back-brand">
      <span class="brand-square"></span>
      <span class="brand-name">Maple Crest Rentals</span>
    </div>
    <p class="services">High End Home Rentals &nbsp;|&nbsp; Land Contract Leasing &nbsp;|&nbsp; Home Remodeling</p>
  </section>
</body>
</html>
```